Calder Mindworks Psychology website transfer from WIX to Wordpress

I have a website currently coded in WIX and I want it (or something like it or better) designed to be coded on Wordpress instead. The website should have mobile optimization so that it can be viewed on mobile devices.

The current website is at: www.caldermindworks.example

I'm not looking for versions of the website that are very different to what I already have, unless they improve on it aesthetically. I'm mainly looking to have a Wordpress version of this website that I built, away from the WIX ecosystem.

Target Market(s)

Psychology services clients

Coding

Coded - Design and coding required

Number of Pages Required

5+ page

Font styles to use
Serif

Requirements
Must have
• The finished product shoud match my website exactly.
Nice to have
• I'm happy to see new ideas that improve on the current website.
Should not have
• It should not be a different version of my website.

```html
<!DOCTYPE html>
<html lang="en">
<head>
<meta charset="utf-8">
<title>Calder Mindworks Psychology</title>
<link rel="stylesheet" href="https://fonts.googleapis.com/css2?family=Fira+Sans:wght@500;600;700&family=Open+Sans:wght@400;600;700&display=swap">
<style>
:root{
  --green:#1f4a3d;
  --navy:#1b3a64;
  --footer:#173452;
  --ink:#1d2b36;
  --blue-text:#2a3f8a;
  --muted:#555f6a;
  --light:#f4f6f9;
  --panel:#eef3f7;
  --white:#ffffff;
  --star:#f2b01e;
}
*{box-sizing:border-box;margin:0;padding:0}
html,body{width:1200px;height:4317px;overflow:hidden;background:var(--white)}
body{font-family:"Open Sans",sans-serif;color:var(--ink)}
.page{position:relative;width:1200px;height:4317px;overflow:hidden;background:var(--white)}
.abs{position:absolute}
h1,h2,h3,h4{font-family:"Fira Sans",sans-serif;font-weight:600}

/* top bar + header */
.topbar{left:0;top:0;width:1200px;height:34px;background:var(--navy);color:#fff;font-size:12px;display:flex;align-items:center;justify-content:center;gap:6px}
.brand{left:74px;top:70px;font-family:"Fira Sans",sans-serif;font-weight:500;font-size:22px;color:var(--green);display:flex;align-items:center;gap:10px}
.brand .dot{width:30px;height:30px;border-radius:50%;border:2px solid var(--green)}
.phone{left:687px;top:58px;font-size:16px;color:var(--navy);display:flex;align-items:center;gap:8px}
.btn-appt{left:858px;top:49px;width:191px;height:40px;background:var(--green);color:#fff;font-size:12px;font-weight:700;display:flex;align-items:center;justify-content:center}
.nav{top:110px;font-size:12px;font-weight:700;color:var(--ink);transform:translateX(-50%)}
.nav.active{color:var(--navy)}
.nav.active::after{content:"";position:absolute;left:-10px;right:-10px;top:30px;height:3px;background:var(--navy)}

/* hero */
.hero{left:0;top:144px;width:1200px;height:700px;background:linear-gradient(90deg,#6f83a8 0%,#a7aec0 35%,#d9c4b3 60%,#e9d8c8 80%,#d4b9a2 100%)}
.hero-wave{left:0;top:700px}
.welcome{left:90px;top:340px;color:#fff;font-size:13px;display:flex;align-items:center;gap:20px}
.welcome::after,.eyebrow::after{content:"";width:46px;height:2px;background:currentColor;display:block}
.hero-title{left:90px;top:370px;width:600px;color:#fff;font-size:43px;line-height:57px;letter-spacing:.5px}
.hero-text{left:90px;top:500px;width:410px;color:#fff;font-size:13.5px;line-height:21px}
.btn{background:var(--green);color:#fff;font-weight:700;font-size:13px;display:flex;align-items:center;justify-content:center;border-radius:4px}

/* shared */
.eyebrow{font-size:12px;font-weight:700;color:var(--ink);display:flex;align-items:center;gap:16px;text-transform:uppercase}
.heading{font-size:47px;color:var(--ink);line-height:62px}
.heading.green{color:var(--green)}
.arrow{width:44px;height:60px;background:#fff;box-shadow:0 2px 8px rgba(0,0,0,.1);display:flex;align-items:center;justify-content:center}

/* services */
.services-bg{left:0;top:846px;width:1200px;height:703px;background:var(--light)}
.card{width:322px;height:401px;background:#fff;box-shadow:0 2px 10px rgba(0,0,0,.06);text-align:center}
.card .photo{position:absolute;left:0;top:0;width:322px;height:210px}
.card .icon{position:absolute;left:127px;top:176px;width:68px;height:68px;border-radius:50%;background:var(--green);display:flex;align-items:center;justify-content:center}
.card h3{position:absolute;left:0;right:0;top:264px;font-size:24px;color:var(--ink)}
.card p{position:absolute;left:30px;right:30px;top:305px;font-size:13px;line-height:24px;color:var(--muted)}
.card .rule{position:absolute;left:141px;top:371px;width:40px;height:2px;background:var(--ink)}

/* treatments */
.lead{font-size:14px;line-height:24px;color:var(--blue-text)}
.feat-title{font-size:16px;font-weight:700;color:var(--navy)}
.feat-text{font-size:14px;line-height:24px;color:var(--blue-text)}

/* about */
.about-panel{left:590px;top:2254px;width:610px;height:401px;background:var(--panel)}
.about-photo{left:0;top:2232px;width:590px;height:446px;border:5px solid var(--green);background:linear-gradient(120deg,#e6e2dc,#a44a35 55%,#6a4b3b)}

/* testimonials */
.t-card{width:320px;height:240px;background:var(--panel);border-radius:26px}
.quote{font-family:"Fira Sans",sans-serif;font-weight:700;font-size:80px;line-height:60px;color:var(--green);letter-spacing:-6px}
.stars{color:var(--star);font-size:17px;letter-spacing:2px}
.t-title{font-size:17px;font-weight:600;color:var(--ink)}
.t-text{font-size:13px;line-height:24px;color:var(--ink)}
.avatar{width:40px;height:40px;border-radius:50%;background:linear-gradient(135deg,#c7b3a1,#5b4a42)}
.t-name{font-family:"Fira Sans",sans-serif;font-size:17px;font-weight:600;color:var(--green)}
.t-role{font-size:11px;color:var(--ink)}

/* contact */
.contact-bg{left:0;top:3312px;width:1200px;height:560px;background:var(--light)}
.field{background:#fff;border:1px solid #e3e7ec;font-size:12px;color:#8a94a0;padding:0 16px;display:flex;align-items:center;border-radius:3px}

/* footer */
.footer{left:0;top:3938px;width:1200px;height:379px;background:var(--footer)}
.f-title{font-size:15px;font-weight:700;color:#fff;text-transform:uppercase}
.f-text{font-size:12px;line-height:21px;color:#fff}
.social{width:37px;height:37px;border:1px solid rgba(255,255,255,.6);display:flex;align-items:center;justify-content:center}
</style>
</head>
<body>
<div class="page">

  <!-- Top bar -->
  <div class="abs topbar">
    <svg width="12" height="14" viewBox="0 0 12 14"><path d="M6 1a4 4 0 0 1 4 4c0 3-4 8-4 8S2 8 2 5a4 4 0 0 1 4-4z" fill="none" stroke="#fff" stroke-width="1.4"/><circle cx="6" cy="5" r="1.4" fill="#fff"/></svg>
    48 Alder Row, Suite 2
  </div>

  <!-- Header -->
  <div class="abs brand"><span class="dot"></span>Calder Mindworks Psychology</div>
  <div class="abs phone">
    <svg width="16" height="16" viewBox="0 0 16 16"><path d="M4 1l3 3-2 2c1 2 3 4 5 5l2-2 3 3-2 3C7 15 1 9 1 3z" fill="var(--navy)"/></svg>
    (555) 014-2290
  </div>
  <div class="abs btn-appt">REQUEST APPOINTMENT</div>
  <div class="abs nav active" style="left:442px">HOME</div>
  <div class="abs nav" style="left:545px">ABOUT US</div>
  <div class="abs nav" style="left:665px">SERVICES</div>
  <div class="abs nav" style="left:789px">OUR TEAM</div>
  <div class="abs nav" style="left:913px">GALLERY</div>
  <div class="abs nav" style="left:1043px">CONTACT US</div>

  <!-- Hero -->
  <div class="abs hero" role="img" aria-label="Photo of a smiling therapist holding a card with a drawn face for a child"></div>
  <svg class="abs hero-wave" width="1200" height="150" viewBox="0 0 1200 150">
    <path d="M0 58 C300 150 700 160 1200 30 L1200 150 L0 150Z" fill="var(--light)"/>
    <path d="M0 58 C300 150 700 160 1200 30" fill="none" stroke="var(--navy)" stroke-width="8"/>
    <path d="M420 120 C700 140 950 100 1200 20 L1200 45 C950 110 700 145 420 120Z" fill="var(--green)"/>
  </svg>
  <div class="abs welcome">Welcome</div>
  <h1 class="abs hero-title">New Perspective<br>for a Better Life</h1>
  <p class="abs hero-text">Lorem ipsum dolor sit amet, consectetur adipiscing elit, sed do eiusmod tempor incididunt ut labore et dolore magna<br>Lorem ipsum dolor sit amet, consectetur adipiscing elit, sed do eiusmod tempor incididunt ut labore et dolore magna</p>
  <div class="abs btn" style="left:90px;top:613px;width:192px;height:41px;border-radius:0">Discover more</div>

  <!-- Services -->
  <div class="abs services-bg"></div>
  <div class="abs eyebrow" style="left:100px;top:925px">Our Treatments</div>
  <h2 class="abs heading" style="left:97px;top:958px">Services We Provide</h2>
  <div class="abs arrow" style="left:1011px;top:944px"><svg width="10" height="16"><path d="M8 2L2 8l6 6" fill="none" stroke="#111" stroke-width="2"/></svg></div>
  <div class="abs arrow" style="left:1064px;top:944px"><svg width="10" height="16"><path d="M2 2l6 6-6 6" fill="none" stroke="#111" stroke-width="2"/></svg></div>

  <div class="abs card" style="left:94px;top:1054px">
    <div class="photo" role="img" aria-label="Photo of a therapist taking notes on a clipboard" style="background:linear-gradient(135deg,#d7d9d6,#8f9196)"></div>
    <div class="icon"><svg width="30" height="30" viewBox="0 0 30 30"><path d="M15 4l9 7-3 11H9L6 11z" fill="none" stroke="#fff" stroke-width="2"/></svg></div>
    <h3>Psychology Therapy</h3>
    <p>Lorem ipsum dolor sit amet, consectetur adi piscing elit sed do eiusmod tmpor</p>
    <div class="rule"></div>
  </div>
  <div class="abs card" style="left:442px;top:1054px">
    <div class="photo" role="img" aria-label="Photo of a smiling family on a sofa" style="background:linear-gradient(135deg,#e8ddd0,#b9957a)"></div>
    <div class="icon"><svg width="30" height="30" viewBox="0 0 30 30"><circle cx="15" cy="10" r="4" fill="none" stroke="#fff" stroke-width="2"/><path d="M7 23h16M10 23l5-8 5 8" fill="none" stroke="#fff" stroke-width="2"/></svg></div>
    <h3>Clinical Supervision</h3>
    <p>Lorem ipsum dolor sit amet, consectetur adi piscing elit sed do eiusmod tmpor</p>
    <div class="rule"></div>
  </div>
  <div class="abs card" style="left:791px;top:1054px">
    <div class="photo" role="img" aria-label="Photo of a young woman in a counselling session" style="background:linear-gradient(135deg,#d9b9a3,#8a7a72)"></div>
    <div class="icon"><svg width="30" height="30" viewBox="0 0 30 30"><circle cx="11" cy="11" r="3.5" fill="none" stroke="#fff" stroke-width="2"/><circle cx="19" cy="11" r="3.5" fill="none" stroke="#fff" stroke-width="2"/><path d="M5 23c0-4 3-6 6-6s6 2 6 6M13 23c0-4 3-6 6-6s6 2 6 6" fill="none" stroke="#fff" stroke-width="2"/></svg></div>
    <h3>Training &amp; Consultancy</h3>
    <p>Lorem ipsum dolor sit amet, consectetur adi piscing elit sed do eiusmod tmpor</p>
    <div class="rule"></div>
  </div>

  <!-- Treatments -->
  <div class="abs eyebrow" style="left:97px;top:1631px">Treatments</div>
  <h2 class="abs heading green" style="left:95px;top:1664px">Strengthening Minds,<br>Healing Hearts</h2>
  <p class="abs lead" style="left:97px;top:1798px;width:470px">Lorem ipsum dolor sit amet, consectetur adipiscing elit, sed do eiusmo empor incididunt ut abore et dolore magna aliqua. Ut enim ad minim iam, quis nostrud exercitation ullamco</p>

  <svg class="abs" style="left:106px;top:1907px" width="32" height="32" viewBox="0 0 32 32"><circle cx="16" cy="16" r="6" fill="none" stroke="var(--ink)" stroke-width="2"/><circle cx="16" cy="16" r="12" fill="none" stroke="var(--ink)" stroke-width="2" stroke-dasharray="5 3"/></svg>
  <div class="abs feat-title" style="left:158px;top:1901px">Quality Assurance</div>
  <div class="abs feat-text" style="left:161px;top:1929px">Lorem ipsum dolor sit amet,<br>consectetur adipiscing</div>

  <svg class="abs" style="left:378px;top:1907px" width="32" height="32" viewBox="0 0 32 32"><circle cx="15" cy="15" r="11" fill="none" stroke="var(--ink)" stroke-width="2"/><circle cx="23" cy="23" r="5" fill="#fff" stroke="var(--ink)" stroke-width="2"/></svg>
  <div class="abs feat-title" style="left:431px;top:1901px">Professional</div>
  <div class="abs feat-text" style="left:434px;top:1929px">Lorem ipsum dolor sit amet,<br>consectetur adipiscing</div>

  <svg class="abs" style="left:106px;top:2004px" width="32" height="32" viewBox="0 0 32 32"><circle cx="16" cy="10" r="6" fill="none" stroke="var(--ink)" stroke-width="2"/><path d="M5 29c0-7 5-10 11-10s11 3 11 10z" fill="none" stroke="var(--ink)" stroke-width="2"/></svg>
  <div class="abs feat-title" style="left:158px;top:1998px">Confidentiality</div>
  <div class="abs feat-text" style="left:161px;top:2026px">Lorem ipsum dolor sit amet,<br>consectetur adipiscing</div>

  <svg class="abs" style="left:380px;top:2004px" width="32" height="32" viewBox="0 0 32 32"><path d="M16 3l11 9-4 15H9L5 12z" fill="none" stroke="var(--ink)" stroke-width="2"/></svg>
  <div class="abs feat-title" style="left:431px;top:1998px">Client-centric</div>
  <div class="abs feat-text" style="left:434px;top:2026px">Lorem ipsum dolor sit amet,<br>consectetur adipiscing</div>

  <div class="abs btn" style="left:104px;top:2112px;width:168px;height:45px">Apply Now</div>

  <svg class="abs" style="left:640px;top:1654px" width="480" height="480" viewBox="0 0 480 480">
    <path d="M20 240 A220 220 0 1 1 240 460" fill="none" stroke="var(--green)" stroke-width="8"/>
  </svg>
  <div class="abs" role="img" aria-label="Photo of a woman talking during a therapy session" style="left:653px;top:1680px;width:444px;height:444px;border-radius:50%;background:radial-gradient(circle at 50% 40%,#d8cdc2,#9ea3a8)"></div>

  <!-- About -->
  <div class="abs about-panel"></div>
  <div class="abs about-photo" role="img" aria-label="Photo of a bearded man writing in a notebook"></div>
  <div class="abs eyebrow" style="left:649px;top:2295px">About Us</div>
  <h2 class="abs heading green" style="left:649px;top:2324px">About Doctor<br>Calder</h2>
  <p class="abs lead" style="left:649px;top:2462px;width:480px">Lorem ipsum dolor sit amet, consectetur adipiscing elit, sed do eiusmo empor incididunt ut abore et dolore magna aliqua. Ut enim ad minim iam, quis nostrud exercitation ullamco</p>
  <div class="abs btn" style="left:649px;top:2566px;width:167px;height:45px">Apply Now</div>

  <!-- Testimonials -->
  <div class="abs eyebrow" style="left:96px;top:2764px">Testimonials</div>
  <h2 class="abs heading green" style="left:93px;top:2796px">What Clients Are Saying</h2>
  <div class="abs arrow" style="left:1006px;top:2782px"><svg width="10" height="16"><path d="M8 2L2 8l6 6" fill="none" stroke="#111" stroke-width="2"/></svg></div>
  <div class="abs arrow" style="left:1059px;top:2782px"><svg width="10" height="16"><path d="M2 2l6 6-6 6" fill="none" stroke="#111" stroke-width="2"/></svg></div>

  <div class="abs t-card" style="left:92px;top:2911px"></div>
  <div class="abs t-card" style="left:441px;top:2911px"></div>
  <div class="abs t-card" style="left:784px;top:2911px"></div>

  <div class="abs quote" style="left:122px;top:2900px">“</div>
  <div class="abs stars" style="left:124px;top:2944px">★★★★★</div>
  <div class="abs t-title" style="left:124px;top:2975px">They are the Best</div>
  <p class="abs t-text" style="left:124px;top:3005px;width:270px">Lorem ipsum dolor sit amet, consectetur adipiscing elit, sed do eiusmod tempor i ncididunt ut labore et dolore magna aliqua. Ut enim ad minim veniam, quis nostrud exercitation ullamco laboris nisi ut</p>
  <div class="abs avatar" role="img" aria-label="Client portrait" style="left:127px;top:3193px"></div>
  <div class="abs t-name" style="left:186px;top:3191px">Jessica</div>
  <div class="abs t-role" style="left:186px;top:3219px">CEO, Abc Company</div>

  <div class="abs quote" style="left:470px;top:2900px">“</div>
  <div class="abs stars" style="left:470px;top:2944px">★★★★★</div>
  <div class="abs t-title" style="left:470px;top:2975px">They are the Best</div>
  <p class="abs t-text" style="left:470px;top:3005px;width:270px">Lorem ipsum dolor sit amet, consectetur adipiscing elit, sed do eiusmod tempor i ncididunt ut labore et dolore magna aliqua. Ut enim ad minim veniam, quis nostrud exercitation ullamco laboris nisi ut</p>
  <div class="abs avatar" role="img" aria-label="Client portrait" style="left:474px;top:3193px"></div>
  <div class="abs t-name" style="left:532px;top:3191px">Jessica</div>
  <div class="abs t-role" style="left:532px;top:3219px">CEO, Abc Company</div>

  <div class="abs quote" style="left:814px;top:2900px">“</div>
  <div class="abs stars" style="left:815px;top:2944px">★★★★★</div>
  <div class="abs t-title" style="left:815px;top:2975px">They are the Best</div>
  <p class="abs t-text" style="left:815px;top:3005px;width:270px">Lorem ipsum dolor sit amet, consectetur adipiscing elit, sed do eiusmod tempor i ncididunt ut labore et dolore magna aliqua. Ut enim ad minim veniam, quis nostrud exercitation ullamco laboris nisi ut</p>
  <div class="abs avatar" role="img" aria-label="Client portrait" style="left:818px;top:3193px"></div>
  <div class="abs t-name" style="left:876px;top:3191px">Jessica</div>
  <div class="abs t-role" style="left:876px;top:3219px">CEO, Abc Company</div>

  <!-- Contact -->
  <div class="abs contact-bg"></div>
  <div class="abs eyebrow" style="left:136px;top:3384px">Get in Touch</div>
  <h2 class="abs heading green" style="left:134px;top:3418px">Contact Us</h2>
  <div class="abs" style="left:138px;top:3488px;font-size:12px;color:var(--muted)">Just send a message, we will answer within 24 hours</div>
  <div class="abs field" style="left:134px;top:3545px;width:198px;height:37px">Your full name</div>
  <div class="abs field" style="left:354px;top:3545px;width:197px;height:37px">Phone Number</div>
  <div class="abs field" style="left:134px;top:3595px;width:198px;height:37px">Mail Address</div>
  <div class="abs field" style="left:354px;top:3595px;width:197px;height:37px">Subject</div>
  <div class="abs field" style="left:134px;top:3647px;width:417px;height:87px;align-items:flex-start;padding-top:12px">Type your message...</div>
  <div class="abs btn" style="left:134px;top:3758px;width:417px;height:35px;font-size:12px">Send Your Message</div>
  <div class="abs" role="img" aria-label="Photo of a woman listening to a counsellor" style="left:608px;top:3397px;width:486px;height:396px;background:linear-gradient(135deg,#3f4b57,#c9b79c 55%,#e6d6bd)"></div>

  <!-- Footer -->
  <svg class="abs" style="left:0;top:3850px" width="1200" height="100" viewBox="0 0 1200 100">
    <path d="M0 80 C300 20 700 0 1200 90 L1200 100 L0 100Z" fill="var(--footer)"/>
    <path d="M450 20 C750 10 1000 40 1200 70 L1200 90 C1000 55 750 25 450 20Z" fill="var(--green)"/>
  </svg>
  <div class="abs footer"></div>

  <div class="abs f-title" style="left:94px;top:4055px">Contact Us</div>
  <svg class="abs" style="left:94px;top:4098px" width="14" height="18" viewBox="0 0 14 18"><path d="M7 1a6 6 0 0 1 6 6c0 4-6 10-6 10S1 11 1 7a6 6 0 0 1 6-6z" fill="#fff"/><circle cx="7" cy="7" r="2" fill="var(--footer)"/></svg>
  <div class="abs f-text" style="left:127px;top:4096px">48 Alder Row, Suite 2<br>Brookfield, Harbor District</div>
  <svg class="abs" style="left:94px;top:4157px" width="15" height="15" viewBox="0 0 16 16"><path d="M4 1l3 3-2 2c1 2 3 4 5 5l2-2 3 3-2 3C7 15 1 9 1 3z" fill="#fff"/></svg>
  <div class="abs f-text" style="left:127px;top:4154px">555 014 2290</div>
  <svg class="abs" style="left:94px;top:4196px" width="17" height="12" viewBox="0 0 17 12"><rect width="17" height="12" fill="#fff"/><path d="M0 0l8.5 7L17 0" fill="none" stroke="var(--footer)" stroke-width="1.4"/></svg>
  <div class="abs f-text" style="left:127px;top:4191px">hello@caldermindworks.example</div>

  <div class="abs brand" style="left:0;width:1200px;top:4008px;justify-content:center;color:#fff;font-size:26px"><span class="dot" style="border-color:#fff"></span>Calder Mindworks Psychology</div>
  <p class="abs f-text" style="left:440px;top:4102px;width:320px;text-align:center">Lorem ipsum dolor sit amet, consectetur adipisc ing elit, sed do eiusmod tempor incididunt bbbbbut bcbbbcbnmx zjzmsmmzm</p>
  <div class="abs social" role="img" aria-label="Social profile link" style="left:538px;top:4185px">
    <svg width="16" height="16" viewBox="0 0 16 16"><path d="M6.5 9.5l3-3M7 4.5l1.5-1.5a2.5 2.5 0 0 1 3.5 3.5L10.5 8M9 11.5L7.5 13A2.5 2.5 0 0 1 4 9.5L5.5 8" fill="none" stroke="#fff" stroke-width="1.5"/></svg>
  </div>
  <div class="abs social" role="img" aria-label="Social profile link" style="left:580px;top:4185px">
    <svg width="16" height="16" viewBox="0 0 16 16"><path d="M2 3h12v8H7l-3 3v-3H2z" fill="none" stroke="#fff" stroke-width="1.5"/></svg>
  </div>
  <div class="abs social" role="img" aria-label="Social profile link" style="left:625px;top:4185px">
    <svg width="16" height="16" viewBox="0 0 16 16"><circle cx="8" cy="8" r="6" fill="none" stroke="#fff" stroke-width="1.5"/><path d="M2 8h12M8 2c2 2 2 10 0 12M8 2c-2 2-2 10 0 12" fill="none" stroke="#fff" stroke-width="1.2"/></svg>
  </div>

  <div class="abs f-title" style="left:972px;top:4055px">Opening Hours</div>
  <div class="abs f-text" style="left:880px;top:4099px;width:192px;text-align:right">Mon - Fri: 9am - to - 6pm</div>
  <div class="abs f-text" style="left:880px;top:4130px;width:192px;text-align:right">Saturday 9am - to - 2pm</div>
  <div class="abs f-text" style="left:880px;top:4162px;width:192px;text-align:right">Sunday : <span style="text-decoration:underline">Closed</span></div>
  <svg class="abs" style="left:1090px;top:4101px" width="16" height="16" viewBox="0 0 16 16"><circle cx="8" cy="8" r="6.5" fill="none" stroke="#fff" stroke-width="1.4"/><path d="M8 4v4h3" fill="none" stroke="#fff" stroke-width="1.4"/></svg>
  <svg class="abs" style="left:1090px;top:4132px" width="16" height="16" viewBox="0 0 16 16"><circle cx="8" cy="8" r="6.5" fill="none" stroke="#fff" stroke-width="1.4"/><path d="M8 4v4h3" fill="none" stroke="#fff" stroke-width="1.4"/></svg>
  <svg class="abs" style="left:1090px;top:4164px" width="16" height="16" viewBox="0 0 16 16"><circle cx="8" cy="8" r="6.5" fill="none" stroke="#fff" stroke-width="1.4"/><path d="M8 4v4h3" fill="none" stroke="#fff" stroke-width="1.4"/></svg>

  <div class="abs" style="left:64px;top:4267px;width:1072px;height:1px;background:rgba(255,255,255,.3)"></div>
  <div class="abs f-text" style="left:0;width:1200px;top:4280px;text-align:center">Calder Mindworks Psychology</div>
</div>
</body>
</html>
```